Business Card Design Project

A business card for a new company in Ontario Canada called Sketch for Growth. It is a consulting company which uses Brixel as the medium for facilitation.

The target market is for senior leaders in healthcare and social services.

Industry/Entity Type

Healthcare

Requirements
Must have
• The name Sketch For Growth
Dana Moreheuse RRT, B Ed (AD ed).
Tacticraft Facililitator (R)

Tag Line
Engaging Transforming and Innovative
The attached logo

danamoreheuse@mailnook.com
555-284-9137
Should not have
• Lime green
Times New Roman or Arial font
Do not include Brixel bricks on the card.

```html
<!DOCTYPE html>
<html lang="en">
<head>
<meta charset="utf-8">
<title>Sketch for Growth – Business Card</title>
<link rel="stylesheet" href="https://fonts.googleapis.com/css2?family=Anton&family=Open+Sans:wght@400;700&display=swap">
<style>
  :root {
    --title-red: #e00000;
    --title-red-dark: #8a0000;
    --ink: #111111;
    --band-grey: #8c8a8a;
    --band-red: #e60000;
    --band-red-deep: #8e0000;
    --board-light: #eeeeee;
    --board-mid: #c9c9c9;
    --board-pink: #d9a9a9;
    --mark-purple: #6a2c8e;
  }
  * { margin: 0; padding: 0; box-sizing: border-box; }
  html, body { width: 1200px; height: 677px; overflow: hidden; background: #ffffff; }
  .card {
    position: relative;
    width: 1200px;
    height: 677px;
    overflow: hidden;
    font-family: "Open Sans", sans-serif;
    color: var(--ink);
  }
  .backdrop {
    position: absolute;
    inset: 0;
    background:
      radial-gradient(circle at 72% 48%, var(--board-mid) 0%, var(--board-pink) 22%, var(--board-light) 45%, var(--board-mid) 70%, #d8d8d8 100%);
  }
  .side-band { position: absolute; top: 0; height: 677px; }
  .side-band--shadow {
    left: 880px;
    width: 40px;
    background: linear-gradient(to right, rgba(0,0,0,0), rgba(0,0,0,0.25));
  }
  .side-band--grey-left { left: 905px; width: 40px; background: var(--band-grey); }
  .side-band--red {
    left: 945px;
    width: 129px;
    background: linear-gradient(to bottom, var(--band-red) 0%, var(--band-red) 25%, var(--band-red-deep) 50%, var(--band-red) 75%, var(--band-red) 100%);
  }
  .side-band--grey-right { left: 1074px; width: 40px; background: var(--band-grey); }
  .brand-title {
    position: absolute;
    left: 92px;
    top: 58px;
    font-family: "Anton", sans-serif;
    font-size: 104px;
    line-height: 1;
    letter-spacing: -1px;
    white-space: nowrap;
    background: linear-gradient(to right, var(--title-red) 0%, var(--title-red) 30%, var(--title-red-dark) 65%, var(--title-red) 100%);
    -webkit-background-clip: text;
    background-clip: text;
    color: transparent;
    filter: drop-shadow(6px 6px 5px rgba(0,0,0,0.45));
  }
  .contact-line { position: absolute; left: 93px; white-space: nowrap; line-height: 1.2; }
  .contact-name { top: 207px; font-size: 39px; font-weight: 700; }
  .contact-role { top: 262px; font-size: 27px; }
  .contact-credentials { top: 340px; font-size: 32px; }
  .tagline { top: 465px; font-size: 29px; }
  .contact-phone { top: 516px; font-size: 37px; }
  .contact-email { top: 564px; font-size: 37px; }
  .brand-mark {
    position: absolute;
    left: 612px;
    top: 296px;
    width: 200px;
    display: flex;
    align-items: center;
    gap: 12px;
  }
  .brand-mark__dot {
    flex: none;
    width: 26px; height: 26px;
    border-radius: 50%;
    background: var(--mark-purple);
  }
  .brand-mark__name {
    font-size: 30px;
    font-weight: 700;
    line-height: 1.15;
    color: var(--mark-purple);
  }
</style>
</head>
<body>
  <main class="card">
    <div class="backdrop" role="img" aria-label="Soft-focus photograph of a dartboard in grey, white and red"></div>

    <div class="side-band side-band--shadow"></div>
    <div class="side-band side-band--grey-left"></div>
    <div class="side-band side-band--red"></div>
    <div class="side-band side-band--grey-right"></div>

    <h1 class="brand-title">Sketch for Growth</h1>

    <p class="contact-line contact-name">Dana Moreheuse</p>
    <p class="contact-line contact-role">Tacticraft Facililitator (R)</p>
    <p class="contact-line contact-credentials">RRT, B Ed (AD ed).</p>

    <div class="brand-mark">
      <span class="brand-mark__dot"></span>
      <span class="brand-mark__name">Sketch for Growth</span>
    </div>

    <p class="contact-line tagline">Engaging Transforming and Innovative</p>
    <p class="contact-line contact-phone">tel: 555-284-9137</p>
    <p class="contact-line contact-email">email: danamoreheuse@mailnook.com</p>
  </main>
</body>
</html>
```